Orvessa Develoipment and Management Corp Web Design Project

Website... Based on logo. Update forthcoming....
Updates

Reason: Extended to include recently completed logo design.

Target Market(s)

Financiers, investors, public officials, and landowners.

Industry/Entity Type

Management

Requirements
Should not have
• No palm trees, mayan ruins, or other Caribbean references.

```html
<!DOCTYPE html>
<html lang="en">
<head>
<meta charset="utf-8">
<title>Orvessa Develoipment and Management Corp</title>
<link href="https://fonts.googleapis.com/css2?family=Roboto:wght@400;500&display=swap" rel="stylesheet">
<style>
:root{
  --green:#9bb93b;
  --green-dark:#86a22c;
  --footer-green:#a3bd3c;
  --ink:#333;
  --muted:#666;
  --grey-band:#ececec;
  --rule:#d6d6d6;
  --night:#2b2d33;
  --white:#fff;
}
*{margin:0;padding:0;box-sizing:border-box}
html,body{width:723px;height:1200px;overflow:hidden;background:var(--white)}
body{position:relative;font-family:'Roboto',sans-serif;color:var(--ink)}
.abs{position:absolute}
/* header */
.brand{left:54px;top:44px}
.brand-name{font-size:18px;font-weight:500;color:var(--green);letter-spacing:1px;display:flex;align-items:center;gap:6px}
.brand-mark{width:9px;height:9px;background:var(--green)}
.brand-tag{font-size:5px;color:#888;margin-top:2px}
.nav{top:41px;left:306px;display:flex;align-items:center;font-size:8px;color:#333}
.nav a{text-decoration:none;color:inherit}
.nav .active{background:var(--green);color:var(--white);width:48px;height:19px;display:flex;align-items:center;justify-content:center;border-radius:2px}
.nav .item{margin-left:19px}
.nav .item:first-of-type{margin-left:19px}
.search{position:absolute;left:651px;top:40px}
/* hero */
.hero{left:0;top:89px;width:723px;height:318px;background:linear-gradient(180deg,#4f4a4c 0%,#7a6a62 18%,#4e5358 40%,#2e343a 70%,#1f2428 100%)}
.hero-title{left:0;top:130px;width:700px;text-align:center;font-size:19px;line-height:27px;color:var(--white);text-shadow:0 1px 3px rgba(0,0,0,.6)}
.dots{left:693px;top:204px;display:flex;flex-direction:column;gap:4.5px}
.dots span{width:6px;height:6px;border-radius:50%;background:var(--white)}
.dots span:first-child{background:var(--green)}
/* welcome */
.welcome-title{left:0;top:430px;width:723px;text-align:center;font-size:15px;color:var(--green)}
.welcome-text{left:62px;top:457px;width:600px;text-align:center;font-size:9.4px;line-height:16.5px;color:#444}
.btn{background:linear-gradient(#a9c74a,#8cab2f);color:var(--white);font-size:9.5px;border-radius:3px;display:flex;align-items:center;justify-content:center}
/* services */
.services{left:0;top:558px;width:723px;height:236px;background:var(--grey-band);border-top:1px solid var(--rule);border-bottom:1px solid var(--rule)}
.services-title{left:59px;top:584px;font-size:14px;color:#222}
.card-photo{width:140px;height:92px;border:2px solid var(--white);box-shadow:0 2px 4px rgba(0,0,0,.3)}
.card-title{width:160px;text-align:center;font-size:11px;color:var(--green)}
.card-text{width:160px;text-align:center;font-size:7.8px;line-height:12px;color:var(--muted)}
/* corp */
.corp-title{left:53px;top:810px;font-size:12.5px;color:var(--green)}
.corp-text{left:54px;top:834px;width:345px;text-align:justify;font-size:7.9px;line-height:15.9px;color:#444}
.video{left:414px;top:812px;width:258px;height:157px;border:1px solid #ccc;background:var(--white);box-shadow:0 1px 3px rgba(0,0,0,.15)}
.video-frame{left:6px;top:5px;width:244px;height:145px;background:linear-gradient(135deg,#7c8a8c,#c9cfcf 45%,#9aa4a5);border-radius:2px;overflow:hidden}
/* footer */
.footer{left:0;top:990px;width:723px;height:139px;background:var(--footer-green);color:var(--white)}
.f-head{font-size:10.5px;font-weight:500;padding-bottom:7px;border-bottom:1px solid rgba(255,255,255,.6)}
.f-text{font-size:7px;line-height:13px}
.newsletter-input{left:506px;top:1077px;width:130px;height:20px;background:var(--white);border:1px solid #ddd;font-size:6.5px;color:#999;padding:6px 7px}
.newsletter-join{left:636px;top:1077px;width:35px;height:20px;background:#111;color:var(--white);font-size:7.5px;font-weight:500;display:flex;align-items:center;justify-content:center}
.bottom{left:0;top:1129px;width:723px;height:71px;background:var(--night)}
.copyright{left:540px;top:1163px;font-size:7.5px;color:var(--white)}
</style>
</head>
<body>

<!-- header -->
<div class="abs brand">
  <div class="brand-name"><span class="brand-mark"></span>ORVESSA</div>
  <div class="brand-tag">Develoipment and Management Corp</div>
</div>
<nav class="abs nav">
  <a class="active" href="#">HOME</a>
  <a class="item" href="#">ABOUT US</a>
  <a class="item" href="#" style="margin-left:29px">SERVICE</a>
  <a class="item" href="#" style="margin-left:29px">BLOG</a>
  <a class="item" href="#" style="margin-left:29px">NEWS</a>
  <a class="item" href="#" style="margin-left:29px">CONTACT</a>
</nav>
<svg class="search" width="20" height="20" viewBox="0 0 20 20">
  <circle cx="10" cy="10" r="9" fill="none" stroke="#8aa83a" stroke-width="1"/>
  <circle cx="9" cy="9" r="3.5" fill="none" stroke="#8aa83a" stroke-width="1.3"/>
  <line x1="11.5" y1="11.5" x2="14" y2="14" stroke="#8aa83a" stroke-width="1.5"/>
</svg>

<!-- hero -->
<div class="abs hero" role="img" aria-label="Aerial view of a city skyline at dusk with skyscrapers"></div>
<div class="abs hero-title" style="top:219px">LOREM IPSUM IS SIMPLY DUMMY TEXT OF THE<br>PRINTING AND TYPESETTING INDUSTRY</div>
<div class="abs dots"><span></span><span></span><span></span><span></span><span></span></div>

<!-- welcome -->
<h1 class="abs welcome-title" style="font-weight:400">WELCOME TO ORVESSA</h1>
<p class="abs welcome-text">Lorem Ipsum has been the industry's standard dummy text ever since the 1500s, when an unknown printer took a galley of type and scrambled it to make a type specimen book. It has survived not only five centuries, but also the leap into electronic typesetting, remaining essentially unchanged. It was popularised in the 1960s with the release of Typemark sheets containing Lorem Ipsum passages,</p>
<a class="abs btn" style="left:325px;top:517px;width:73px;height:24px">Read More</a>

<!-- services -->
<section class="abs services"></section>
<h2 class="abs services-title" style="font-weight:400">SERVICES</h2>
<svg class="abs" style="left:624px;top:581px" width="44" height="18" viewBox="0 0 44 18">
  <circle cx="9" cy="9" r="8" fill="none" stroke="#111" stroke-width="1.5"/>
  <path d="M10.5 5.5 7 9l3.5 3.5" fill="none" stroke="#111" stroke-width="1.5"/>
  <circle cx="34" cy="9" r="8" fill="none" stroke="#111" stroke-width="1.5"/>
  <path d="M32.5 5.5 36 9l-3.5 3.5" fill="none" stroke="#111" stroke-width="1.5"/>
</svg>

<div class="abs card-photo" style="left:55px;top:614px;background:linear-gradient(135deg,#e4e8ec,#b9c3cc)" role="img" aria-label="Photo of officials in a meeting room"></div>
<div class="abs card-photo" style="left:212px;top:614px;background:linear-gradient(135deg,#9a9c9e,#d6d8da)" role="img" aria-label="Photo of investors around a desk"></div>
<div class="abs card-photo" style="left:370px;top:614px;background:linear-gradient(135deg,#d9d5cf,#6c7378)" role="img" aria-label="Photo of stakeholders talking at a table"></div>
<div class="abs card-photo" style="left:528px;top:614px;background:linear-gradient(135deg,#9fb6c8,#4d5a66)" role="img" aria-label="Photo of a businessman in an office"></div>

<div class="abs card-title" style="left:36px;top:718px">Public Officials</div>
<div class="abs card-title" style="left:195px;top:718px">Investors</div>
<div class="abs card-title" style="left:358px;top:718px">Project Stakeholders</div>
<div class="abs card-title" style="left:518px;top:718px">Landowners</div>
<div class="abs card-text" style="left:44px;top:737px">Lorem Ipsum is simply dummy text of the printing and typesetting industry</div>
<div class="abs card-text" style="left:202px;top:737px">Lorem Ipsum is simply dummy text of the printing and typesetting industry</div>
<div class="abs card-text" style="left:360px;top:737px">Lorem Ipsum is simply dummy text of the printing and typesetting industry</div>
<div class="abs card-text" style="left:519px;top:737px">Lorem Ipsum is simply dummy text of the printing and typesetting industry</div>

<!-- corporation -->
<h2 class="abs corp-title" style="font-weight:400">DEVELOPMENT &amp; MANAGEMENT CORPORATION</h2>
<p class="abs corp-text">Lorem Ipsum has been the industry's standard dummy text ever since the 1500s, when an unknown printer took a galley of type and scrambled it to make a type specimen book. It has survived not only five centuries, but also the leap into electronic typesetting, remaining essentially unchanged. It was popularised in the 1960s with the release of Typemark sheets containing Lorem Ipsum passages, and more recently with desktop publishing software like Quillset PageForge including versions of Lorem Ipsum.</p>
<a class="abs btn" style="left:55px;top:952px;width:73px;height:25px">Read More</a>

<div class="abs video">
  <div class="abs video-frame" role="img" aria-label="Video still of a team working over plans at a table">
    <svg class="abs" style="left:107px;top:55px" width="30" height="30" viewBox="0 0 30 30">
      <circle cx="15" cy="15" r="14" fill="rgba(60,60,60,.6)"/>
      <path d="M12 9l9 6-9 6z" fill="#fff"/>
    </svg>
    <svg class="abs" style="left:0;top:126px" width="244" height="19" viewBox="0 0 244 19">
      <rect width="244" height="19" fill="#1e1e1e"/>
      <circle cx="13" cy="10" r="4" fill="none" stroke="#fff" stroke-width="1.2"/>
      <rect x="28" y="8" width="4" height="4" fill="#e04040"/>
      <rect x="36" y="7" width="20" height="5" fill="#e04040" opacity=".7"/>
      <rect x="62" y="9" width="125" height="2" fill="#555"/>
      <rect x="62" y="9" width="45" height="2" fill="#e04040"/>
      <text x="192" y="12.5" font-family="Roboto,sans-serif" font-size="5.5" fill="#fff">01:30 / 04:55</text>
      <rect x="219" y="7" width="7" height="5" fill="none" stroke="#fff"/>
      <circle cx="234" cy="10" r="2.5" fill="#fff"/>
    </svg>
  </div>
</div>

<!-- footer -->
<footer class="abs footer"></footer>
<div class="abs" style="left:55px;top:1015px;width:157px;color:#fff">
  <div class="f-head">LATEST NEWS</div>
  <div class="f-text" style="margin-top:8px">27/JULY/2014</div>
  <div class="f-text" style="text-align:justify">Donec consectetur diam ac nibh auctor ultricies. Integer mauris lacus, consequat in luctus id, semper sed felis. Cum sociis natoque penatibus</div>
  <div class="f-text" style="text-align:right;margin-top:2px;font-size:6px">READ MORE &#187;</div>
</div>
<div class="abs" style="left:257px;top:1018px;width:55px;color:#fff">
  <div class="f-head">LINK</div>
  <div class="f-text" style="margin-top:9px;line-height:14.7px">About us<br>Services<br>Presentation<br>Clients</div>
</div>
<div class="abs" style="left:347px;top:1015px;width:124px;color:#fff">
  <div class="f-head" style="border-bottom:none">GET IN TOUCH</div>
  <div class="f-text" style="margin-top:8px;line-height:12px">4180 N. Harbor View Rd. Suite 900<br>Linwood, FL 32011</div>
  <div class="f-text" style="margin-top:4px;line-height:14.5px">Phone 407-555-0148<br>Email: hello@orvessa-corp.test</div>
</div>
<div class="abs" style="left:507px;top:1015px;width:164px;color:#fff">
  <div class="f-head">NEWSLETTER</div>
  <div class="f-text" style="margin-top:10px">Join our mailing list to stay up to date and get notices about our new releases!</div>
</div>
<div class="abs newsletter-input">hello@orvessa-corp.test</div>
<div class="abs newsletter-join">JOIN</div>

<!-- bottom bar -->
<div class="abs bottom"></div>
<div class="abs" style="left:54px;top:1168px">
  <div style="font-size:13px;font-weight:500;color:var(--green);letter-spacing:1px;display:flex;align-items:center;gap:5px"><span style="width:7px;height:7px;background:var(--green)"></span>ORVESSA</div>
  <div style="font-size:4px;color:#777;margin-top:1px">Develoipment and Management Corp</div>
</div>
<svg class="abs" style="left:308px;top:1157px" width="68" height="18" viewBox="0 0 68 18">
  <circle cx="9" cy="9" r="8" fill="#d8d8d8"/>
  <circle cx="34" cy="9" r="8" fill="#d8d8d8"/>
  <circle cx="59" cy="9" r="8" fill="#d8d8d8"/>
</svg>
<div class="abs copyright">Copyright &copy; 2014&nbsp; All Rights Reserved</div>

</body>
</html>
```